Wedding Program

Miriam and Owen are getting married. They are looking for a simple 4-page program that conveys the special day. Venue is a museum in a large East-Coast city: classic 18th century, formal. Ceremony is non-religious. Party includes a photo booth and DJ.

He's a math geek - she's an activist/educator.

Please incorporate unique design sensibility - be creative! Colors of purple, eggplant, ivory, and gray are the couple's choice. Fall motif OK.

Target Market(s)

ages 25 - 85, members of a family

Industry/Entity Type

Graphic Design

Font styles to use
Serif
Decorative

Colors
8769ae
b7a5cd
fece3e
f78f20
757575
cfcfcf
6b449b
a64599
fffaee

Requirements
Must have
• Readable, attractive 4-color design using the copy and image provided in the attachment.
Nice to have
• It's a LOVE-ly day for a wedding - be creative!
Should not have
• Avoid flowery girly-girl fonts or obvious hearts and flowers stuff.

```html
<!DOCTYPE html>
<html lang="en">
<head>
<meta charset="utf-8">
<title>Wedding Program – Miriam &amp; Owen</title>
<link rel="stylesheet" href="https://fonts.googleapis.com/css2?family=Felipa&family=Gabriela&family=Jost:wght@400&display=swap">
<style>
  :root {
    --backdrop: #1c1c1c;
    --paper: #fdfcfe;
    --purple: #6b449b;
    --purple-soft: #8769ae;
    --lavender: #b7a5cd;
    --toile: #e6e0ee;
    --label: #7a6a92;
  }
  * { margin: 0; padding: 0; box-sizing: border-box; }
  html, body { width: 1200px; height: 900px; overflow: hidden; background: var(--backdrop); }
  .canvas { position: relative; width: 1200px; height: 900px; background: var(--backdrop); }

  .page {
    position: absolute; top: 180px; height: 564px;
    background: var(--paper); overflow: hidden;
  }
  .page--party { left: 30px; width: 582px; }
  .page--ceremony { left: 638px; width: 532px; }

  .toile {
    position: absolute; inset: 0;
    background:
      radial-gradient(ellipse 40% 30% at 25% 55%, var(--toile), transparent 70%),
      radial-gradient(ellipse 35% 25% at 75% 80%, var(--toile), transparent 70%),
      radial-gradient(ellipse 30% 22% at 80% 40%, #ece7f2, transparent 70%),
      var(--paper);
  }
  .crest {
    position: absolute; top: 0; left: 50%; transform: translateX(-50%);
    height: 110px;
    background: linear-gradient(180deg, var(--purple-soft) 0%, var(--lavender) 60%, rgba(183,165,205,0) 100%);
    border-radius: 0 0 40% 40% / 0 0 60% 60%;
    opacity: .85;
  }
  .page--party .crest { width: 490px; }
  .page--ceremony .crest { width: 520px; }

  .title {
    position: absolute; left: 0; right: 0; text-align: center;
    font-family: "Felipa", cursive; color: var(--purple);
    font-size: 40px; line-height: 1; top: 130px;
  }

  .role, .name { position: absolute; text-align: center; white-space: nowrap; transform: translateX(-50%); }
  .role {
    font-family: "Jost", sans-serif; font-size: 9px; letter-spacing: .8px;
    text-transform: uppercase; color: var(--label);
  }
  .name { font-family: "Gabriela", serif; font-size: 17px; color: var(--purple); }

  .order {
    position: absolute; top: 186px; left: 0; right: 0; list-style: none; text-align: center;
    font-family: "Gabriela", serif; font-size: 16px; line-height: 25px; color: var(--purple);
  }
</style>
</head>
<body>
<main class="canvas">

  <section class="page page--party">
    <div class="toile" role="img" aria-label="Faint lavender toile pattern of pastoral scenes"></div>
    <div class="crest" role="img" aria-label="Purple baroque scrollwork ornament"></div>
    <h1 class="title">The Wedding Party</h1>

    <p class="role" style="left:290px;top:184px">Bride and Groom</p>
    <p class="name" style="left:290px;top:198px">Miriam (Mimi) Ashby and Owen Delmont</p>

    <p class="role" style="left:152px;top:236px">Bride's Parents</p>
    <p class="name" style="left:152px;top:248px">Warren and Celeste Ashby</p>
    <p class="role" style="left:410px;top:236px">Groom's Parents</p>
    <p class="name" style="left:410px;top:248px">Harold and Joan Delmont</p>

    <p class="role" style="left:290px;top:275px">Bridesmaids</p>
    <p class="name" style="left:290px;top:288px">Nora Delmont, Tessa Lindqvist, Clara Beaumont</p>

    <p class="role" style="left:290px;top:326px">Groomsmen</p>
    <p class="name" style="left:290px;top:340px">Felix Delmont, Martin Ashby, Derek Holloway, Arjun Mehrotra</p>

    <p class="role" style="left:290px;top:366px">Grandparent of the Bride</p>
    <p class="name" style="left:290px;top:378px">Evelyn Marchetti</p>
    <p class="role" style="left:290px;top:406px">Grandparents of the Groom</p>
    <p class="name" style="left:290px;top:418px">Walter Delmont, Henry Caldwell</p>

    <p class="role" style="left:290px;top:465px">Celebrant</p>
    <p class="name" style="left:290px;top:476px">Lydia Fairbanks</p>
  </section>

  <section class="page page--ceremony">
    <div class="toile" role="img" aria-label="Faint lavender toile pattern of pastoral scenes"></div>
    <div class="crest" role="img" aria-label="Purple baroque scrollwork ornament"></div>
    <h1 class="title">The Ceremony</h1>
    <ol class="order">
      <li>Processional</li>
      <li>Greeting</li>
      <li>Blessing of the Rings</li>
      <li>Presentation of the Bride and Groom</li>
      <li>Reading: Edwin Thorne, The Orchards of Linden Hill</li>
      <li>Promises and Wedding Vows</li>
      <li>Exchange of Wedding Rings</li>
      <li>Wine Box and Love Letters</li>
      <li>Signing of Marriage Certificate</li>
      <li>Declaration of Support</li>
      <li>Reading: Samuel Grey, The Long Road Home</li>
      <li>Declaration of Marriage and The Kiss</li>
      <li>Recessional</li>
    </ol>
  </section>

</main>
</body>
</html>
```